Independent Financial Advisor Billboard Campaign - Granite Bridge Financial

I am a local, independent financial advisor. My company is Granite Bridge Financial, located in Charleston, WV. My main source of revenue comes from those nearing or entering retirement that need assistance with financial planning and investment management. Many are looking to rollover their employer retirement plan into an IRA account. I would like a billboard design campaign that focuses on this type of client. Please see our website www.granitebridgefinancial-example.com for more information.

```html
<!DOCTYPE html>
<html lang="en">
<head>
<meta charset="utf-8">
<title>Granite Bridge Financial – Billboard</title>
<link rel="stylesheet" href="https://fonts.googleapis.com/css2?family=Open+Sans:wght@400;600&display=swap">
<style>
  :root {
    --page-bg: #f2f2f2;
    --board-gray: #e8e8e8;
    --board-white: #ffffff;
    --ring-white: #ffffff;
    --accent-dark: #4b4752;
    --brand-navy: #1f3f73;
    --text-gray: #3f3f44;
    --photo-light: #b0704f;
    --photo-dark: #6e4330;
  }
  * { margin: 0; padding: 0; box-sizing: border-box; }
  html, body {
    width: 1200px;
    height: 1075px;
    overflow: hidden;
    background: var(--page-bg);
    font-family: "Open Sans", Arial, sans-serif;
  }
  .billboard {
    position: absolute;
    left: 40px;
    top: 268px;
    width: 841px;
    height: 405px;
    transform: scale(1.3317);
    transform-origin: 0 0;
    overflow: hidden;
    background: var(--board-gray);
  }
  .billboard__shapes {
    position: absolute;
    inset: 0;
    width: 841px;
    height: 405px;
  }
  .brand {
    position: absolute;
    left: 74px;
    top: 110px;
    display: flex;
    align-items: center;
    gap: 10px;
    color: var(--brand-navy);
    font-weight: 600;
  }
  .brand__mark {
    width: 30px;
    height: 30px;
    background: var(--brand-navy);
  }
  .brand__name {
    font-size: 19px;
    line-height: 1.05;
    letter-spacing: 0.3px;
  }
  .brand__name span {
    display: block;
    font-size: 10px;
    letter-spacing: 5px;
    text-align: center;
  }
  .message {
    position: absolute;
    left: 68px;
    top: 248px;
    color: var(--text-gray);
  }
  .message__title {
    font-size: 13px;
    letter-spacing: 1px;
    font-weight: 400;
  }
  .message__body {
    margin-top: 3px;
    font-size: 8.4px;
    line-height: 16px;
    width: 280px;
  }
  .message__call {
    margin-top: 14px;
    font-size: 17px;
    letter-spacing: 0.2px;
  }
  .message__web {
    margin-top: 12px;
    font-size: 12px;
    letter-spacing: 0.6px;
  }
</style>
</head>
<body>
  <div class="billboard">
    <svg class="billboard__shapes" viewBox="0 0 841 405">
      <defs>
        <linearGradient id="photoTone" x1="0" y1="0" x2="1" y2="1">
          <stop offset="0" stop-color="var(--photo-light)"/>
          <stop offset="1" stop-color="var(--photo-dark)"/>
        </linearGradient>
      </defs>
      <path class="panel-white" fill="var(--board-white)"
            d="M0 0 H324 C352 60 350 140 337 187 C390 205 440 240 452 300 L452 405 H0 Z"/>
      <circle class="ring" cx="607" cy="-10" r="40" fill="none" stroke="var(--ring-white)" stroke-width="5"/>
      <circle class="ring" cx="835" cy="5" r="28" fill="none" stroke="var(--ring-white)" stroke-width="5"/>
      <circle class="ring" cx="20" cy="-10" r="28" fill="none" stroke="var(--board-gray)" stroke-width="5"/>
      <circle class="ring" cx="374" cy="420" r="46" fill="none" stroke="var(--board-gray)" stroke-width="5"/>
      <circle class="dot" cx="373" cy="35" r="11" fill="var(--ring-white)"/>
      <circle class="dot" cx="562" cy="59" r="4" fill="var(--ring-white)"/>
      <circle class="dot" cx="591" cy="85" r="11" fill="var(--ring-white)"/>
      <circle class="corner-accent" cx="0" cy="405" r="66" fill="var(--accent-dark)"/>
      <circle class="advisor-photo" cx="641" cy="313" r="200" fill="url(#photoTone)"
              role="img" aria-label="Photo of the advisor seated at his desk in front of a brick wall"/>
    </svg>

    <div class="brand">
      <div class="brand__mark"></div>
      <div class="brand__name">Granite Bridge<span>FINANCIAL</span></div>
    </div>

    <div class="message">
      <h2 class="message__title">RETIRE WITH CONFIDENCE</h2>
      <p class="message__body">Rolling over your employer retirement plan into an IRA? Local, independent planning and investment guidance.</p>
      <p class="message__call">CALL US NOW (304) 555-0142</p>
      <p class="message__web">www.granitebridgefinancial-example.com</p>
    </div>
  </div>
</body>
</html>
```